Moroccan Wordpress Q'vora Exhibit Design

We seek a new website for Q’vora (LantrelVaults.example), an exhibit of The Kelmoth Initiative’s Terra-Hall of Coastal Heritage Studies, dedicated to uncovering the “buried” or “covered” Jewish treasures of Morocco.
Spanning the entire country, from metropolitan centers to remote villages, Q’vora proffers a virtual passport to visitors wishing to explore mountain-top shrines of Jewish “saints” that continue to be voluntarily protected by Muslim caretakers, scorpion-guarded genizot (burial grounds for holy texts and objects), anthropomorphic tombstones in seaside cemeteries, synagogues on the edge of the Sahara Desert, and ancient urban quarters with hidden reminders of their one-time residents.
This exhibit marks the first public showing of documentation on the majority of these sites, including several Vichy regime desert labor and “discipline” camps where hundreds of Jews and non-Jewish political prisoners toiled, suffered torture, and died during the Holocaust.
Q’vora is certainly the first to feature:
* Extensive documentation on Jewish sites in major cities and remote settings alike;
* Exclusive immersive panoramas, three-dimensional reconstructions, high-definition videos, site summaries, cultural atlas, archival and contemporary photos; and
* Interactive virtual tours of sites led by Morocco’s only Jewish guide.
Q'vora's website design needs to be clean and informational and exciting as well as showcase the best of our collection. The winning design should include an intuitive interface and taxonomy capable of handling hundreds of site entries.
The template should also have a distinctive homepage, themed pages (curator's introduction, staff, screening rooms to view multimedia content, virtual tours, behind-the-scenes, contribute), and no blog elements (e.g., comment section). Admin friendliness is a plus.

```html
<!DOCTYPE html>
<html lang="en">
<head>
<meta charset="utf-8">
<title>Q'vora : Jewish Treasures of Southern Morocco</title>
<link rel="stylesheet" href="https://fonts.googleapis.com/css2?family=Carlito&family=PT+Sans&family=Playball&display=swap">
<style>
  :root {
    --paper-top: #f4f3ef;
    --paper-mid: #f3e3c4;
    --paper-bottom: #e2b57e;
    --title: #b5632a;
    --subtitle: #e0731f;
    --body-text: #a45f1f;
    --nav-text: #ec6e1c;
    --ring: #e8893f;
    --divider: #e9c46a;
    --frame: #d9915a;
    --ruin-dark: #7a4a2c;
    --ruin-light: #c58a55;
  }
  * { margin: 0; padding: 0; box-sizing: border-box; }
  html, body { width: 1200px; height: 900px; overflow: hidden; }
  body {
    position: relative;
    background: linear-gradient(to bottom, var(--paper-top) 0, var(--paper-top) 437px, var(--paper-mid) 470px, var(--paper-bottom) 900px);
    font-family: "PT Sans", Tahoma, sans-serif;
  }
  .hero-frames { position: absolute; left: 0; top: 92px; }
  .hero-photo {
    position: absolute; left: 0; top: 94px; width: 398px; height: 327px;
    background: linear-gradient(135deg, #9a8470 0%, #b9a48d 35%, #8e7a66 60%, #3f6fb5 80%, #6d5a4a 100%);
  }
  .hero-landscape {
    position: absolute; left: 565px; top: 160px; width: 635px; height: 277px;
    background:
      radial-gradient(ellipse 45% 55% at 42% 65%, rgba(122,74,44,0.85) 0%, rgba(138,86,52,0.6) 45%, rgba(197,138,85,0) 100%),
      radial-gradient(ellipse 70% 40% at 70% 95%, rgba(197,138,85,0.7) 0%, rgba(214,184,153,0.3) 60%, rgba(214,184,153,0) 100%);
  }
  .divider { position: absolute; left: 0; top: 437px; width: 1200px; height: 1px; background: var(--divider); }
  .site-title {
    position: absolute; right: 78px; top: 83px;
    font-family: "Carlito", Calibri, sans-serif; font-weight: 400;
    font-size: 33px; color: var(--title); text-align: right; white-space: nowrap;
  }
  .site-subtitle {
    position: absolute; right: 79px; top: 127px;
    font-family: "Carlito", Calibri, sans-serif; font-size: 20px; color: var(--subtitle); white-space: nowrap;
  }
  .main-nav { position: absolute; left: 28px; top: 456px; list-style: none; }
  .main-nav li { display: flex; align-items: center; height: 50px; margin-bottom: 28px; }
  .main-nav li:nth-child(3) { margin-bottom: 22px; }
  .nav-thumb {
    width: 50px; height: 50px; border-radius: 50%;
    border: 4px solid var(--ring); flex: none;
  }
  .nav-label {
    font-family: "Playball", cursive; font-size: 21px; color: var(--nav-text);
    margin-left: 12px; text-decoration: none;
  }
  .intro { position: absolute; left: 416px; top: 473px; width: 745px; color: var(--body-text); font-size: 13.4px; line-height: 16px; }
  .intro p { margin-bottom: 16px; }
  .copyright { position: absolute; left: 416px; top: 875px; font-size: 10.5px; color: var(--body-text); }
</style>
</head>
<body>
  <svg class="hero-frames" width="430" height="334" aria-hidden="true">
    <g fill="none" stroke="var(--frame)" stroke-width="1">
      <rect x="0.5" y="0.5" width="425" height="331"/>
      <rect x="0.5" y="1.5" width="420" height="329"/>
      <rect x="0.5" y="2.5" width="414" height="327"/>
      <rect x="0.5" y="3.5" width="408" height="325"/>
      <rect x="0.5" y="4.5" width="403" height="323"/>
    </g>
  </svg>
  <div class="hero-photo" role="img" aria-label="Interior of a restored synagogue with plastered walls, a hanging lantern and a blue painted railing"></div>

  <div class="hero-landscape" role="img" aria-label="Illustration of a ruined earthen kasbah on a rocky hill"></div>

  <h1 class="site-title">Q'vora : Jewish Treasures of Southern Morocco</h1>
  <p class="site-subtitle">Presented by the Kelmoth Initiative the Halvern Foundation</p>

  <div class="divider"></div>

  <ul class="main-nav">
    <li><span class="nav-thumb" role="img" aria-label="Red earth doorway" style="background:radial-gradient(circle,#b65a2a,#6e2f14)"></span><a class="nav-label" href="#">Q'vora</a></li>
    <li><span class="nav-thumb" role="img" aria-label="Desert path" style="background:linear-gradient(#d79a6c,#a8552f)"></span><a class="nav-label" href="#">Tour</a></li>
    <li><span class="nav-thumb" role="img" aria-label="Lit panorama interior" style="background:radial-gradient(circle,#fffbe8 0,#c4c0a8 25%,#3b3a32 70%)"></span><a class="nav-label" href="#">Panoramas</a></li>
    <li><span class="nav-thumb" role="img" aria-label="Standing stone marker" style="background:linear-gradient(90deg,#c9c3b6,#5d5550 50%,#d8d2c6)"></span><a class="nav-label" href="#">Contact</a></li>
  </ul>

  <main class="intro">
    <p>Jewish heritage tours of Morocco typically cycle through Casablanca, Tangiers, Fez, and Marrakesh. But the Jewish Moroccan heartland lies south of these metropolitan centers, in the towns and villages of the Atlas mountains and Sahara desert. Here, Jewish life punctuated the landscape, legendary rabbis helped sustain rural communities, and a distinctive Judeo-Amazigh (Berber) culture developed over the course of two millennia.</p>
    <p>Decades after the community’s dissolution, the once-vibrant Jewish heritage these sites embody is ubiquitous yet hidden, seemingly indelible but inevitably fading. Where it still exists, it does so behind unmarked walls, just off treacherous dirt trails, deep within mountains, in the annual pilgrimages (hillulot) that attract hundreds of expatriates — and increasingly only in the memories of aging Muslim former neighbors as well as the superstitions that they have bequeathed to their children and grand children. Q’vora means “covered” or “buried” in the Moroccan dialect, a fitting–and, in some cases, literal–description of what remains.</p>
    <p>During the Holocaust, France’s Vichy regime established a series of forced labor and “discipline” camps in the region’s far eastern flank where hundreds of Jews and non-Jewish political prisoners toiled and died in the desert. These sites are similarly forgotten, but are important reminders of North Africa’s Holocaust history that has only in recent years begun to attract scholarly interest.</p>
    <p>This exhibit marks the first time that pictures of the majority of these sites (including several Vichy camps) have been made public. In addition to photographs, we present an array of virtual documentation–concise summaries, video tours, oral history recordings, 360-degree panoramas, and geo-mapping data–to provide an exclusive glimpse into the heartland of Jewish heritage in Morocco.</p>
    <p>Come explore these remarkable sites on a unique tour — made possible with the generous support of the Halvern Foundation.</p>
  </main>

  <footer class="copyright">Copyright © 2010 Terrace Atlas Mapping, Inc. All Rights Reserved.</footer>
</body>
</html>
```